complete redesign of VitaPlate.com

VITAPLATE.COM
MAIN MANU

We need it cut into HTML / Wordpress Friendly.... Our developer will handle all the WP / PHP coding, but we need it placed into HTML format so he can put into wordpress.

Please see the old vitaplate.com by visiting www.vitaplate.com... we want something completely different, but... just use this site for reference as to audience, theme, etc... we want something where it is science meets diet in helping fight cancer :)

WE NEED SOMETHING MORE MODERN AND MEDICAL IN TERMS OF DESIGN

See below:

1 CANCER NEWS
2 NUTRITION DIAGNOSTICS
3 DIET STEPS
4 DIET SUPPLEMENTS IN CANCER 
5 DICTIONARY OF MARKINGS ON FOOD
6 FERNAMEAL VIDEOS
7 YOUR INDIVIDUAL DIET - SUBSCRIPTION

a. CANCER NEWS - latest articles relating to cancer prevention research treatments

b. NUTRITION DIAGNOSTICS -  description of the research that must be done to determine the degree of malnutrition of the body a place on the charts
pictures, etc.

c. DIET STEPS 
(sub menu - @)
¥ prevention of oncological - @
¥ diet chemotherapy - @
¥ diet in radiotherapy - @
¥ hormonal diet - @
¥ diet during convalescence - @

d. DIET SUPPLEMENTS IN CANCER - articles describing various supplements summary tables, etc.

e. DICTIONARY OF MARKINGS ON FOOD - composition, translation of labels on food, itd.

f. FERNAMEAL VIDEOS 
(sub menu - @)
¥ healthy cooking - @
¥ meal preparation - @
¥ storage of food - @
¥ eco food - @
¥ rehabilitation - @
¥ yoga - @
¥ exercises - @
¥ psycho-oncology training - @
¥ music therapy - @

g. YOUR INDIVIDUAL DIET -  individual personalized diet for subscribing. We
add this point by developing a system of diet.

After 3 months, we will add special individual programs that mix diet, exercise and psychological lectures

Industry/Entity Type

Medical

Logo Text

Vita Plate / VitaPlate.com

Number of Pages Required

5+ page

Font styles to use
Sans Serif

Colors
ec1f27
9bcb3c
ffffff

Requirements
Must have
• HTML/CSS

```html
<!DOCTYPE html>
<html lang="en">
<head>
<meta charset="utf-8">
<title>VitaPlate – Nutrition Diet</title>
<link href="https://fonts.googleapis.com/css2?family=Roboto:wght@300;400;500;700&display=swap" rel="stylesheet">
<style>
:root{
  --blue:#1e7fd3;
  --blue-dark:#1566b3;
  --blue-panel:#3a86c9;
  --red:#e0262d;
  --orange:#f05a1e;
  --ink:#333;
  --muted:#666;
  --light:#f3f3f3;
  --dark:#2b2622;
  --white:#fff;
}
*{margin:0;padding:0;box-sizing:border-box}
html,body{width:1200px;height:3315px;overflow:hidden}
body{font-family:'Roboto',Arial,sans-serif;color:var(--ink);background:var(--white);position:relative}
section,header,footer,nav{position:absolute;left:0;width:1200px}
.abs{position:absolute}

/* header */
.site-header{top:0;height:122px;background:var(--light)}
.header-notch{left:395px;top:0;width:450px;height:122px;background:var(--white);clip-path:polygon(0 0,100% 0,92% 100%,8% 100%)}
.contact-top{left:97px;top:36px;font-size:15px;line-height:22px;color:var(--muted)}
.contact-top .phone{color:var(--blue)}
.contact-icon{left:97px;top:40px;width:36px;height:36px}
.contact-top{left:140px}
.brand{left:520px;top:20px;width:160px;text-align:center}
.brand-dot{display:block;width:46px;height:46px;border-radius:50%;background:var(--red);margin:0 auto 8px}
.brand-name{font-size:20px;font-weight:500;color:var(--ink);letter-spacing:1px}
.search{left:872px;top:40px;width:228px;height:34px;background:var(--white);border:1px solid #e2e2e2;font-size:12px;color:var(--ink);padding:9px 10px}
.search svg{position:absolute;right:10px;top:9px}

.main-nav{top:122px;height:55px;background:linear-gradient(var(--blue),var(--blue-dark))}
.main-nav ul{list-style:none;display:flex;justify-content:space-between;padding:0 97px;height:55px;align-items:center}
.main-nav a{color:var(--white);font-size:12.5px;font-weight:500;text-decoration:none;letter-spacing:.3px}

/* hero */
.hero{top:177px;height:548px;background:linear-gradient(90deg,#7f97a0 0%,#a9bcc3 40%,#d5dde0 70%,#e9eef0 100%);overflow:hidden}
.hero-photo{right:0;top:0;width:720px;height:548px;background:radial-gradient(ellipse at 60% 40%,#f1ede8 0%,#dcd8d4 45%,rgba(220,225,228,0) 75%)}
.hero-title{left:97px;top:195px;font-size:52px;font-weight:500;color:var(--white);letter-spacing:-.5px}
.hero-text{left:97px;top:267px;font-size:15px;line-height:21px;color:var(--white);width:380px}
.btn{display:inline-block;color:var(--white);font-size:15px;text-align:center;border-radius:24px;text-decoration:none}
.hero-btn{left:97px;top:326px;width:170px;height:46px;line-height:46px;background:var(--orange);box-shadow:0 2px 0 #b73c0c}
.dots{left:99px;top:396px;display:flex;gap:6px}
.dots span{width:13px;height:13px;border-radius:50%;border:2px solid var(--white)}
.dots span.on{background:var(--white)}

/* section titles */
.sec-title{width:1200px;text-align:center;font-size:32px;font-weight:400;letter-spacing:1px;color:#222}
.divider{left:400px;width:400px;height:20px}
.lead{left:160px;width:880px;text-align:center;font-size:11.5px;line-height:21px;color:var(--muted)}

.welcome{top:725px;height:519px}
.tile{top:217px;width:289px;height:247px;overflow:hidden}
.tile-bg{inset:0}
.tile-shade{inset:0;background:rgba(0,0,0,.35)}
.tile-plus{left:122px;top:104px;width:44px;height:44px}
.tile-name{top:152px;width:100%;text-align:center;font-size:19px;color:var(--white)}
.tile-text{top:177px;width:100%;text-align:center;font-size:12px;line-height:18px;color:var(--white);padding:0 50px}

.steps{top:1244px;height:502px;background:linear-gradient(180deg,#3a332c 0%,#241f1b 50%,#3a2f27 100%)}
.steps .sec-title{color:var(--white);font-size:38px;top:50px}
.steps .lead{color:#ddd;top:145px}
.step{top:241px;width:172px;height:172px;border-radius:50%;border:3px solid var(--white);background:linear-gradient(135deg,#3d93e0,#1462bd);text-align:center;color:var(--white)}
.step svg{margin-top:28px}
.step-label{font-size:12.5px;font-weight:500;line-height:16px;margin-top:8px}

.news-video{top:1746px;height:457px}
.col-title{top:45px;font-size:26px;color:#222}
.news-item{left:97px;width:545px;height:120px}
.news-thumb{left:0;top:0;width:173px;height:117px}
.news-head{left:190px;top:0;font-size:16px;color:#333}
.news-date{left:190px;top:28px;font-size:11.5px;color:var(--blue)}
.news-text{left:190px;top:52px;width:355px;font-size:11.5px;line-height:21px;color:var(--muted)}
.news-rule{left:190px;top:140px;width:355px;height:1px;background:#e2e2e2}
.video{left:696px;top:99px;width:404px;height:288px;border:1px solid #ddd}
.video-frame{left:0;top:0;width:402px;height:258px;background:linear-gradient(135deg,#e8e4dc,#c8b8a8 60%,#b84a3e)}
.video-bar{left:0;top:258px;width:402px;height:28px;background:#f4f4f4}

.diagnostics{top:2203px;height:504px;background:var(--blue-panel);color:var(--white)}
.diag-title{left:97px;top:110px;font-size:38px;font-weight:400;line-height:44px}
.diag-title b{font-size:50px;font-weight:500;display:block;line-height:56px}
.diag-text{left:97px;top:222px;width:490px;font-size:11.5px;line-height:20px}
.diag-list{left:97px;top:300px;list-style:none;font-size:12.5px;line-height:26px}
.diag-list li::before{content:"";display:inline-block;width:10px;height:10px;border-radius:50%;background:var(--white);margin-right:14px;vertical-align:-1px}
.diag-art{left:660px;top:70px;width:430px;height:380px;background:radial-gradient(circle at 50% 55%,#5c9ed6 0%,#3a86c9 70%);border-radius:8px}

.supplements{top:2707px;height:327px}
.supp-btn{left:497px;top:234px;width:206px;height:44px;line-height:44px;background:var(--red);box-shadow:0 3px 0 #8c1217}

.site-footer{top:3034px;height:230px;background:var(--light)}
.foot-title{top:38px;font-size:15px;color:#333;letter-spacing:.5px}
.foot-line{font-size:12.5px;line-height:18px;color:#333}
.foot-small{font-size:11.5px;line-height:17px;color:#444}
.foot-ago{font-size:11px;color:#444;font-weight:500}
.field{width:226px;height:38px;background:var(--white);border:1px solid #e0e0e0;font-size:11.5px;padding:11px 14px;color:#333}
.sub-btn{width:88px;height:32px;line-height:32px;background:#1f2a36;color:var(--white);font-size:11.5px;text-align:center}
.foot-brand{left:948px;top:70px;width:160px;text-align:center}
.bottom-bar{top:3264px;height:51px;background:var(--blue);color:var(--white);font-size:12px;text-align:center;line-height:51px}
</style>
</head>
<body>

<header class="site-header">
  <div class="abs header-notch"></div>
  <svg class="abs contact-icon" viewBox="0 0 36 36" width="36" height="36" aria-hidden="true"><circle cx="18" cy="18" r="16" fill="none" stroke="#1e7fd3" stroke-width="2"/><path d="M13 11c1 0 2 3 2 4s-2 1-1 3 3 4 4 4 1-2 2-1 3 2 3 3-2 3-4 2-9-6-9-11c0-2 2-4 3-4z" fill="#1e7fd3"/></svg>
  <div class="abs contact-top"><div class="phone">+1 555 014 2290 07</div><div>info@vitaplate.com</div></div>
  <div class="abs brand"><span class="brand-dot"></span><span class="brand-name">VITAPLATE</span></div>
  <div class="abs search">SEARCH<svg width="14" height="14" viewBox="0 0 14 14"><circle cx="6" cy="6" r="4.5" fill="none" stroke="#333" stroke-width="2"/><line x1="9.5" y1="9.5" x2="13" y2="13" stroke="#333" stroke-width="2"/></svg></div>
</header>

<nav class="main-nav">
  <ul>
    <li><a href="#">HOME</a></li>
    <li><a href="#">CANCER NEWS</a></li>
    <li><a href="#">NUTRITION DIAGNOSTICS</a></li>
    <li><a href="#">DIET STEPS</a></li>
    <li><a href="#">DIET SUPPLEMENTS IN CANCER</a></li>
    <li><a href="#">FERNAMEAL VIDEOS</a></li>
    <li><a href="#">CONTACT US</a></li>
  </ul>
</nav>

<section class="hero">
  <div class="abs hero-photo" role="img" aria-label="Doctor holding a capsule filled with fresh vegetables"></div>
  <h1 class="abs hero-title">NUTRITION DIET</h1>
  <p class="abs hero-text">Nemo enim ipsam voluptatem quia voluptas sit aspernatur aut odit aut fugit, sed quia</p>
  <a class="abs btn hero-btn" href="#">READ MORE INFO</a>
  <div class="abs dots"><span class="on"></span><span></span><span></span></div>
</section>

<section class="welcome">
  <h2 class="abs sec-title" style="top:45px">WELCOME TO VITAPLATE</h2>
  <svg class="abs divider" style="top:95px" viewBox="0 0 400 20"><line x1="0" y1="10" x2="180" y2="10" stroke="#ccc"/><polyline points="180,10 188,10 192,3 197,17 201,6 205,10 220,10" fill="none" stroke="#999" stroke-width="1.5"/><line x1="220" y1="10" x2="400" y2="10" stroke="#ccc"/></svg>
  <p class="abs lead" style="top:128px">Lorem ipsum dolor sit amet, consectetur adipiscing elit, sed do eiusmod tempor incididunt ut labore et dolore magna aliqua. Ut enim ad minim veniam, quis nostrud exercitation ullamco laboris nisi ut aliquip ex ea commodo consequat. Duis aute irure dolor in reprehenderit in voluptate velit esse cillum dolore eu fugiat nulla pariatur. Excepteur sint occaecat cupidatat non proident, sunt in culpa qui officia deserunt mollit anim id est laborum</p>

  <div class="abs tile" style="left:150px">
    <div class="abs tile-bg" role="img" aria-label="Broccoli and red cabbage on a table" style="background:linear-gradient(135deg,#4d6a3a,#6a4a48 60%,#8a2a3a)"></div>
    <div class="abs tile-shade"></div>
    <svg class="abs tile-plus" viewBox="0 0 44 44"><circle cx="22" cy="22" r="20" fill="none" stroke="#fff" stroke-width="2"/><path d="M22 12v20M12 22h20" stroke="#fff" stroke-width="4"/></svg>
    <div class="abs tile-name">VITAPLATE</div>
    <div class="abs tile-text">Nemo enim ipsam voluptatem quia voluptas sit aspernatur</div>
  </div>
  <div class="abs tile" style="left:451px">
    <div class="abs tile-bg" role="img" aria-label="Smiling woman in a headband" style="background:linear-gradient(135deg,#c9b49a,#a88264 60%,#6f5544)"></div>
    <div class="abs tile-shade"></div>
    <svg class="abs tile-plus" viewBox="0 0 44 44"><circle cx="22" cy="22" r="20" fill="none" stroke="#fff" stroke-width="2"/><path d="M22 12v20M12 22h20" stroke="#fff" stroke-width="4"/></svg>
    <div class="abs tile-name">YOUR INDIVIDUAL DIET</div>
    <div class="abs tile-text">Nemo enim ipsam voluptatem quia voluptas sit aspernatur</div>
  </div>
  <div class="abs tile" style="left:751px">
    <div class="abs tile-bg" role="img" aria-label="Pill bottles and medication on a desk" style="background:linear-gradient(135deg,#6a3a32,#8a6a5a 55%,#b9b1a8)"></div>
    <div class="abs tile-shade"></div>
    <svg class="abs tile-plus" viewBox="0 0 44 44"><circle cx="22" cy="22" r="20" fill="none" stroke="#fff" stroke-width="2"/><path d="M22 12v20M12 22h20" stroke="#fff" stroke-width="4"/></svg>
    <div class="abs tile-name">CANCER NEWS</div>
    <div class="abs tile-text">Nemo enim ipsam voluptatem quia voluptas sit aspernatur</div>
  </div>
</section>

<section class="steps" role="img" aria-label="Dimmed background of fresh fruit and vegetables">
  <h2 class="abs sec-title">DIET STEPS</h2>
  <svg class="abs divider" style="top:108px" viewBox="0 0 400 20"><line x1="0" y1="10" x2="180" y2="10" stroke="#aaa"/><polyline points="180,10 188,10 192,3 197,17 201,6 205,10 220,10" fill="none" stroke="#fff" stroke-width="1.5"/><line x1="220" y1="10" x2="400" y2="10" stroke="#aaa"/></svg>
  <p class="abs lead">Lorem ipsum dolor sit amet, consectetur adipiscing elit, sed do eiusmod tempor incididunt ut labore et dolore magna aliqua. Ut enim ad minim veniam, quis nostrud exercitation ullamco laboris nisi ut aliquip ex ea commodo consequat. Duis aute irure dolor in reprehenderit</p>

  <div class="abs step" style="left:120px"><svg width="56" height="56" viewBox="0 0 56 56"><circle cx="28" cy="28" r="24" fill="none" stroke="#fff" stroke-width="3"/><circle cx="20" cy="22" r="5" fill="#fff"/><circle cx="34" cy="20" r="5" fill="#fff"/><circle cx="36" cy="34" r="5" fill="#fff"/><circle cx="22" cy="36" r="5" fill="#fff"/></svg><div class="step-label">PREVENTION OF<br>ONCOLOGICAL</div></div>
  <div class="abs step" style="left:316px"><svg width="56" height="56" viewBox="0 0 56 56"><circle cx="26" cy="30" r="22" fill="none" stroke="#fff" stroke-width="3"/><path d="M30 4a22 22 0 0 1 22 22H30z" fill="#fff"/><line x1="26" y1="30" x2="10" y2="44" stroke="#fff" stroke-width="3"/></svg><div class="step-label">DIET<br>CHEMOTHERAPY</div></div>
  <div class="abs step" style="left:513px"><svg width="56" height="56" viewBox="0 0 56 56"><path d="M8 16a28 28 0 0 0 40 26z" fill="none" stroke="#fff" stroke-width="3"/><path d="M14 18l14 18M22 16l8 20M32 16l0 20" stroke="#fff" stroke-width="2"/></svg><div class="step-label">DIET IN<br>RADIOTHERAPY</div></div>
  <div class="abs step" style="left:710px"><svg width="56" height="56" viewBox="0 0 56 56"><circle cx="28" cy="32" r="18" fill="none" stroke="#fff" stroke-width="3"/><path d="M28 32V22M28 32l7 5" stroke="#fff" stroke-width="3"/><rect x="23" y="6" width="10" height="7" fill="#fff"/></svg><div class="step-label">HORMONAL<br>DIET</div></div>
  <div class="abs step" style="left:906px"><svg width="56" height="56" viewBox="0 0 56 56"><rect x="16" y="6" width="24" height="8" rx="2" fill="#fff"/><rect x="12" y="16" width="32" height="36" rx="5" fill="none" stroke="#fff" stroke-width="3"/><line x1="12" y1="30" x2="44" y2="30" stroke="#fff" stroke-width="3"/></svg><div class="step-label">DIET DURING<br>CONVALESCENCE</div></div>
</section>

<section class="news-video">
  <h2 class="abs col-title" style="left:97px">CANCER NEWS</h2>
  <h2 class="abs col-title" style="left:696px">FERNAMEAL VIDEOS</h2>

  <article class="abs news-item" style="top:99px">
    <div class="abs news-thumb" role="img" aria-label="Young woman exercising outdoors" style="background:linear-gradient(135deg,#7fae3a,#c8583a 60%,#e9c7a8)"></div>
    <h3 class="abs news-head">Nemo Enim Ipsam Voluptatem</h3>
    <div class="abs news-date">DEC 12, 2015</div>
    <p class="abs news-text">Lorem ipsum dolor sit amet, consectetur adipiscing elit, sed do eiusmod tempor incididunt ut labore et dolore magna aliqua. Ut enim ad minim veniam, quis nostrud</p>
    <div class="abs news-rule"></div>
  </article>
  <article class="abs news-item" style="top:272px">
    <div class="abs news-thumb" role="img" aria-label="Smiling older couple outdoors" style="background:linear-gradient(135deg,#c99a3a,#d8b48e 55%,#6a8a3a)"></div>
    <h3 class="abs news-head">Nemo Enim Ipsam Voluptatem</h3>
    <div class="abs news-date">DEC 12, 2015</div>
    <p class="abs news-text">Lorem ipsum dolor sit amet, consectetur adipiscing elit, sed do eiusmod tempor incididunt ut labore et dolore magna aliqua. Ut enim ad minim veniam, quis nostrud</p>
  </article>

  <div class="abs video">
    <div class="abs video-frame" role="img" aria-label="Woman preparing a healthy meal in a kitchen"></div>
    <svg class="abs" style="left:173px;top:101px" width="56" height="56" viewBox="0 0 56 56"><circle cx="28" cy="28" r="25" fill="rgba(255,255,255,.4)" stroke="#333" stroke-width="3"/><path d="M22 17l16 11-16 11z" fill="#333"/></svg>
    <div class="abs video-bar">
      <svg width="402" height="28" viewBox="0 0 402 28"><path d="M12 9l7 5-7 5z" fill="#333"/><text x="30" y="18" font-size="8" fill="#333" font-family="Roboto,sans-serif">00:00/03:03</text><rect x="110" y="12" width="210" height="4" fill="#ccc"/><rect x="110" y="12" width="150" height="4" fill="var(--red)"/><path d="M342 11h3l4-3v12l-4-3h-3z" fill="#333"/><rect x="356" y="12" width="36" height="4" fill="var(--red)"/></svg>
    </div>
  </div>
</section>

<section class="diagnostics">
  <h2 class="abs diag-title">NUTRITION<b>DIAGNOSTICS</b></h2>
  <p class="abs diag-text">Lorem ipsum dolor sit amet, consectetur adipiscing elit, sed do eiusmod tempor incididunt ut labore et dolore magna aliqua. Ut enim ad minim veniam, quis nostrud exercitation ullamco laboris nisi ut aliquip ex ea commodo consequat. Duis aute irure dolor</p>
  <ul class="abs diag-list">
    <li>Nemo enim ipsam voluptatem quia voluptas</li>
    <li>Sed ut perspiciatis unde omnis iste natus</li>
    <li>Neque porro quisquam est, qui</li>
  </ul>
  <div class="abs diag-art" role="img" aria-label="Human figure linked to icons of a capsule, microscope, watermelon, test tubes and DNA"></div>
</section>

<section class="supplements">
  <h2 class="abs sec-title" style="top:42px">DIET SUPPLEMENTS IN CANCER</h2>
  <svg class="abs divider" style="top:92px" viewBox="0 0 400 20"><line x1="0" y1="10" x2="180" y2="10" stroke="#ccc"/><polyline points="180,10 188,10 192,3 197,17 201,6 205,10 220,10" fill="none" stroke="#999" stroke-width="1.5"/><line x1="220" y1="10" x2="400" y2="10" stroke="#ccc"/></svg>
  <p class="abs lead" style="top:140px">Lorem ipsum dolor sit amet, consectetur adipiscing elit, sed do eiusmod tempor incididunt ut labore et dolore magna aliqua. Ut enim ad minim veniam, quis nostrud exercitation ullamco laboris nisi ut aliquip ex ea commodo consequat. Duis aute irure dolor in reprehenderit in voluptate velit esse cillum dolore eu fugiat nulla pariatur. Excepteur sint occaecat cupidatat non proident, sunt in culpa qui officia deserunt mollit anim id est laborum</p>
  <a class="abs btn supp-btn" href="#">DIET SUPPLEMENTS</a>
</section>

<footer class="site-footer">
  <h4 class="abs foot-title" style="left:97px">CONTACT US</h4>
  <svg class="abs" style="left:97px;top:74px" width="18" height="26" viewBox="0 0 18 26"><path d="M9 1a8 8 0 0 0-8 8c0 6 8 16 8 16s8-10 8-16a8 8 0 0 0-8-8z" fill="#888"/><circle cx="9" cy="9" r="3" fill="#f3f3f3"/></svg>
  <div class="abs foot-line" style="left:135px;top:74px">VITAPLATE.COM<br>1418 West Alder Lane,<br>Springfield OREGON 97401, USA.</div>
  <svg class="abs" style="left:97px;top:143px" width="20" height="20" viewBox="0 0 20 20"><path d="M5 2c1 0 3 4 3 5s-2 1-1 3 3 4 4 4 1-2 2-1 4 2 4 3-2 3-4 3S2 13 2 6c0-2 2-4 3-4z" fill="#888"/></svg>
  <div class="abs foot-line" style="left:135px;top:144px;font-size:15px">+1 05 5550 1862</div>
  <svg class="abs" style="left:97px;top:173px" width="20" height="14" viewBox="0 0 20 14"><rect x="1" y="1" width="18" height="12" fill="none" stroke="#888" stroke-width="1.5"/><path d="M1 1l9 7 9-7" fill="none" stroke="#888" stroke-width="1.5"/></svg>
  <div class="abs foot-line" style="left:135px;top:172px">info@VITAPLATE.COM</div>

  <h4 class="abs foot-title" style="left:390px">RECENT EVENTS</h4>
  <div class="abs" style="left:390px;top:72px;width:240px"><p class="foot-small">Lorem ipsum dolor sit amet, consectetur adipiscing elit, sed do eiusmod</p><p class="foot-ago" style="margin-top:8px">3 days ago</p></div>
  <div class="abs" style="left:390px;top:140px;width:240px"><p class="foot-small">Lorem ipsum dolor sit amet, consectetur adipiscing elit, sed do eiusmod</p><p class="foot-ago" style="margin-top:8px">3 days ago</p></div>

  <h4 class="abs foot-title" style="left:666px">SIGN UP FOR NEWSLETTER</h4>
  <div class="abs field" style="left:666px;top:74px">Enter Name</div>
  <div class="abs field" style="left:666px;top:121px">Enter Email</div>
  <div class="abs sub-btn" style="left:800px;top:124px">SUBSCRIBE</div>

  <div class="abs foot-brand"><span class="brand-dot" style="width:60px;height:60px"></span><span class="brand-name">VITAPLATE</span></div>
</footer>

<div class="abs bottom-bar" style="position:absolute;left:0;width:1200px">©2014 - 2015 VITAPLATE.COM., All Rights Reserved.</div>

</body>
</html>
```